Sharp, new and modern business flyer

We are an industrial crate manufacturer whose core customer base is in the aeronautical parts sector. We also however build very custom travel show crates and road cases for any spectrum of industries. We have a substantial facility and can accommodate large, production orders so we would like to attract large, local businesses if possible, but ship crates nationwide as well. We have an old tri fold flyer that we have been using for over 3+ years that I will attach for reference but it desperately needs a fresh new look and complete revamp! Our slogan is "Innovative Crating With Superior Service." We are known in the industry as being extremely fast as well as providing excellent customer service and crate design work. We have also in the last year, added two globes to the background of our logo. I am attaching our current business cards that show how we incorporate that. Feel free to visit our website as well as our Facebook page for more info and current pictures. Both are Palbrook-freight.com.

Target Market(s)

Mid to large local business and corporations. Industrial and manufacturing - especially aeronautical or medical (delicate surgical equipment) as well as military.

Industry/Entity Type

Manufacturer

Font styles to use
Sans Serif
Other font styles liked:
• Stencil

Colors

Designer to choose colors to be used in the design.

Requirements
Must have
• 1. Current photos and descriptions of our capabilities. Our most current products are on our Facebook page and our capabilities are on our website.
• 2. Our flyer must state that "All of our quality products are built with lumber that is ISPM 15 Heat Treatment Certified"
• 3. Please add custom pallets as well as on-site crating
Nice to have
• A new, modern look that shows us as current and growing.
Should not have
• Woman owned listed...we are no longer woman owned.

```html
<!DOCTYPE html>
<html lang="en">
<head>
<meta charset="UTF-8">
<title>Palbrook-freight.com – Tri-fold Brochure</title>
<link rel="stylesheet" href="https://fonts.googleapis.com/css2?family=Anton&family=Open+Sans:wght@400;600&display=swap">
<style>
  :root{
    --stage:#dedede;
    --gold:#f3b73f;
    --gold-light:#f7c75e;
    --ink:#1b1916;
    --wood:#d9c39a;
    --wood-dark:#b99d6c;
    --case-orange:#f39a1c;
    --case-yellow:#efe02a;
    --crate-pink:#e7c4b2;
  }
  *{box-sizing:border-box;margin:0;padding:0}
  html,body{width:1200px;height:800px;overflow:hidden;background:var(--stage)}
  body{display:flex;align-items:center;justify-content:center;font-family:"Open Sans",sans-serif;color:var(--ink)}
  .brochure{display:flex;width:1080px;height:760px;box-shadow:0 10px 30px rgba(0,0,0,.18)}
  .panel{position:relative;width:360px;height:760px;background:linear-gradient(180deg,var(--gold-light),var(--gold));display:flex;flex-direction:column;overflow:hidden}
  .panel + .panel{border-left:1px solid rgba(0,0,0,.08)}
  .panel-body{flex:1;padding:36px 30px 20px}
  .footer-band{height:48px;flex:none;background:var(--ink);color:var(--gold);display:flex;align-items:center;justify-content:center;gap:10px;font-weight:600;font-size:16px;letter-spacing:.3px;white-space:nowrap}
  .footer-band svg{width:16px;height:16px}
  .display{font-family:"Anton",sans-serif;font-style:italic;font-weight:400;line-height:1.1}

  /* products panel */
  .products-title{font-size:27px;margin-bottom:14px}
  .product-list{list-style:none;font-size:15px;line-height:1.45}
  .product-list li{display:flex;gap:10px;align-items:flex-start}
  .product-list svg{flex:none;width:13px;height:13px;margin-top:5px}
  .photo-collage{margin-top:18px;height:212px;border-radius:2px;background:linear-gradient(135deg,var(--wood) 0%,var(--wood-dark) 35%,var(--case-orange) 55%,var(--case-yellow) 75%,#3a3835 100%)}

  /* about panel */
  .about-text{font-size:14px;line-height:1.5;text-align:center}
  .certified{font-size:14px;line-height:1.5;text-align:center;font-weight:600;margin-top:12px}
  .ship-line{font-size:20px;text-align:center;margin:24px 0 20px}
  .mini-mark{display:flex;align-items:center;justify-content:center;gap:8px;margin-bottom:22px}
  .mark-square{width:22px;height:22px;background:var(--ink);flex:none}
  .mark-name{font-family:"Open Sans",sans-serif;font-weight:600;font-size:16px;white-space:nowrap}
  .contact{font-size:14px;line-height:1.7;text-align:center;font-style:normal}
  .contact-row{display:flex;align-items:center;justify-content:center;gap:6px;white-space:nowrap}
  .contact-row svg{width:14px;height:14px;flex:none}

  /* cover panel */
  .cover-mark{display:flex;align-items:center;justify-content:center;gap:12px;margin-top:30px;padding:44px 0;border:6px solid var(--ink)}
  .cover-mark .mark-square{width:30px;height:30px}
  .cover-mark .mark-name{font-size:21px}
  .slogan{font-family:"Anton",sans-serif;font-size:17px;text-align:center;margin:22px 0 16px;letter-spacing:.3px;text-transform:uppercase}
  .solve{display:flex;gap:12px;align-items:flex-start}
  .solve-text{font-family:"Anton",sans-serif;font-weight:400;line-height:1.05;width:140px}
  .solve-text .big{font-size:36px;display:block}
  .solve-text .mid{font-size:20px;display:block}
  .solve-text .small{font-size:16px;display:block}
  .crate-photo{flex:1;height:150px;background:linear-gradient(160deg,var(--crate-pink) 0%,#d8b29e 45%,var(--wood) 70%,var(--wood-dark) 100%)}
  .crate-photo.lower{margin-top:14px;height:150px;background:linear-gradient(140deg,var(--wood) 0%,#efe3cc 40%,var(--wood-dark) 100%)}
</style>
</head>
<body>
<main class="brochure">

  <section class="panel panel-products">
    <div class="panel-body">
      <h2 class="display products-title">Our Quality Products and Services Include:</h2>
      <ul class="product-list">
        <li><svg viewBox="0 0 14 14"><path d="M1 7l4 4 8-9" fill="none" stroke="#1b1916" stroke-width="2"/></svg>Custom Crates</li>
        <li><svg viewBox="0 0 14 14"><path d="M1 7l4 4 8-9" fill="none" stroke="#1b1916" stroke-width="2"/></svg>Production Crates</li>
        <li><svg viewBox="0 0 14 14"><path d="M1 7l4 4 8-9" fill="none" stroke="#1b1916" stroke-width="2"/></svg>Military Crates</li>
        <li><svg viewBox="0 0 14 14"><path d="M1 7l4 4 8-9" fill="none" stroke="#1b1916" stroke-width="2"/></svg>Custom Corrugated Cardboard Boxes</li>
        <li><svg viewBox="0 0 14 14"><path d="M1 7l4 4 8-9" fill="none" stroke="#1b1916" stroke-width="2"/></svg>Road Cases</li>
        <li><svg viewBox="0 0 14 14"><path d="M1 7l4 4 8-9" fill="none" stroke="#1b1916" stroke-width="2"/></svg>Heavy Equipment Skidding &amp; Crating</li>
        <li><svg viewBox="0 0 14 14"><path d="M1 7l4 4 8-9" fill="none" stroke="#1b1916" stroke-width="2"/></svg>Trade Show Crates &amp; Cases</li>
        <li><svg viewBox="0 0 14 14"><path d="M1 7l4 4 8-9" fill="none" stroke="#1b1916" stroke-width="2"/></svg>Collapsible Crates</li>
        <li><svg viewBox="0 0 14 14"><path d="M1 7l4 4 8-9" fill="none" stroke="#1b1916" stroke-width="2"/></svg>Stretch &amp; Shrink Wrapping</li>
        <li><svg viewBox="0 0 14 14"><path d="M1 7l4 4 8-9" fill="none" stroke="#1b1916" stroke-width="2"/></svg>Shock Control Systems</li>
        <li><svg viewBox="0 0 14 14"><path d="M1 7l4 4 8-9" fill="none" stroke="#1b1916" stroke-width="2"/></svg>International Wood Pallets</li>
        <li><svg viewBox="0 0 14 14"><path d="M1 7l4 4 8-9" fill="none" stroke="#1b1916" stroke-width="2"/></svg>Custom Pallets</li>
        <li><svg viewBox="0 0 14 14"><path d="M1 7l4 4 8-9" fill="none" stroke="#1b1916" stroke-width="2"/></svg>On-Site Crating</li>
      </ul>
      <div class="photo-collage" role="img" aria-label="Collage of photos: plywood shipping crates, an orange road case, a yellow trade show case and black equipment cases"></div>
    </div>
    <footer class="footer-band">
      <svg viewBox="0 0 16 16"><circle cx="8" cy="8" r="7" fill="none" stroke="#f3b73f" stroke-width="1.5"/><path d="M1 8h14M8 1c-3 4-3 10 0 14M8 1c3 4 3 10 0 14" fill="none" stroke="#f3b73f" stroke-width="1.2"/></svg>
      www.palbrook-freight.com
    </footer>
  </section>

  <section class="panel panel-about">
    <div class="panel-body">
      <p class="about-text">Our services include shipping crates, military crates, road cases, heavy equipment crating, on-site crating, custom pallets and rugged corrugated cardboard boxes. Beginning with no-cost design and consulting services, we suggest ways to improve a container's performance. Our brand new, enlarged modern facility and experienced staff provide fast delivery of all sizes and quantities of quality products. IPPC certification also allows all of our products to deliver international shipping solutions. We are anxious to exceed your expectations!</p>
      <p class="certified">All of our quality products are built with lumber that is ISPM 15 Heat Treatment Certified.</p>
      <h3 class="display ship-line">WE SHIP ANYWHERE IN THE U.S.A.</h3>
      <div class="mini-mark">
        <span class="mark-square"></span>
        <span class="mark-name">Palbrook-freight.com</span>
      </div>
      <address class="contact">
        <div class="contact-row"><svg viewBox="0 0 14 14"><path d="M7 1a4 4 0 0 0-4 4c0 3 4 8 4 8s4-5 4-8a4 4 0 0 0-4-4z" fill="none" stroke="#1b1916" stroke-width="1.5"/><circle cx="7" cy="5" r="1.4" fill="#1b1916"/></svg>1840 W. Cedarline Road, United States</div>
        <div class="contact-row">Marlow, FL 33460</div>
        <div class="contact-row"><svg viewBox="0 0 14 14"><circle cx="7" cy="7" r="6" fill="none" stroke="#1b1916" stroke-width="1.3"/><path d="M5 4l1 2-1 1c.5 1 1 1.5 2 2l1-1 2 1-.5 1.5C7 11 4 8 3.5 5.5z" fill="#1b1916"/></svg>(561) 555-0147 / (561) 555-0182</div>
        <div class="contact-row"><svg viewBox="0 0 14 14"><rect x="1" y="3" width="12" height="8" fill="none" stroke="#1b1916" stroke-width="1.3"/><path d="M1 3l6 5 6-5" fill="none" stroke="#1b1916" stroke-width="1.3"/></svg>dana@palbrook-freight.com</div>
      </address>
    </div>
    <footer class="footer-band">
      <svg viewBox="0 0 16 16"><circle cx="8" cy="8" r="7" fill="none" stroke="#f3b73f" stroke-width="1.5"/><path d="M1 8h14M8 1c-3 4-3 10 0 14M8 1c3 4 3 10 0 14" fill="none" stroke="#f3b73f" stroke-width="1.2"/></svg>
      www.palbrook-freight.com
    </footer>
  </section>

  <section class="panel panel-cover">
    <div class="panel-body">
      <div class="cover-mark">
        <span class="mark-square"></span>
        <span class="mark-name">Palbrook-freight.com</span>
      </div>
      <p class="slogan">Innovative Crating With Superior Service</p>
      <div class="solve">
        <h1 class="solve-text">
          <span class="big">WE SOLVE</span>
          <span class="mid">CUSTOMER'S</span>
          <span class="small">PRODUCT CRATING AND</span>
          <span class="mid">STORAGE PROBLEMS!</span>
        </h1>
        <div class="crate-photo" role="img" aria-label="Photo of a pink corrugated crate with work gloves on top"></div>
      </div>
      <div class="crate-photo lower" role="img" aria-label="Photo of an open plywood shipping crate on a pallet base"></div>
    </div>
    <footer class="footer-band">
      <svg viewBox="0 0 16 16"><circle cx="8" cy="8" r="7" fill="none" stroke="#f3b73f" stroke-width="1.5"/><path d="M1 8h14M8 1c-3 4-3 10 0 14M8 1c3 4 3 10 0 14" fill="none" stroke="#f3b73f" stroke-width="1.2"/></svg>
      www.palbrook-freight.com
    </footer>
  </section>

</main>
</body>
</html>
```